Harbourline Residence Suites

I'm looking for a four page graphic design (home page, search summary/results page, apartment details page, generic information page for content such as FAQ and thank you for submitting forms etc). The pages will be used to develop a web application to promote serviced apartments throughout Africa. Although the business is based in Africa, apartments will be offered to clients across the globe. Apartments will also be situated worldwide.

Target Market(s)

Target audience is business and individual travellers looking for short stays in apartments worldwide.

Number of Pages Required

4 pages

Requirements
Must have
• Clean professional design

```html
<!DOCTYPE html>
<html lang="en">
<head>
<meta charset="utf-8">
<title>Harbourline Residence Suites</title>
<link href="https://fonts.googleapis.com/css2?family=Noto+Sans:wght@400&display=swap" rel="stylesheet">
<style>
  :root {
    --black: #000000;
    --brand-red: #9b1408;
    --gold-top: #e0b00a;
    --olive-mid: #b5b20e;
    --gold-bottom: #e4ac05;
    --stripe-light: #f7ef8a;
    --stripe-dark: #b8980a;
    --field-grey: #85826f;
    --footer-grey: #9a9a9a;
    --white: #ffffff;
    --ink: #111111;
  }
  * { margin: 0; padding: 0; box-sizing: border-box; }
  html, body { width: 1200px; height: 900px; overflow: hidden; background: var(--black); }
  body { font-family: "Noto Sans", "Segoe UI", sans-serif; position: relative; }

  .site-header { position: absolute; left: 0; top: 0; width: 1200px; height: 190px; background: var(--black); }
  .brand-name {
    position: absolute; left: 0; width: 1200px; top: 58px;
    text-align: center; color: var(--white);
    font-size: 44px; font-weight: 400; letter-spacing: 2px; text-transform: uppercase;
    padding-right: 150px;
  }

  .header-stripe {
    position: absolute; left: 0; top: 190px; width: 1200px; height: 15px;
    background: linear-gradient(to bottom, var(--stripe-light) 0%, #f2e05a 40%, var(--stripe-dark) 100%);
  }

  .page-body {
    position: absolute; left: 0; top: 205px; width: 1200px; height: 580px;
    background: linear-gradient(to bottom, var(--gold-top) 0%, var(--olive-mid) 45%, var(--olive-mid) 55%, var(--gold-bottom) 100%);
  }

  .main-nav { position: absolute; left: 110px; top: 280px; width: 195px; }
  .main-nav a {
    display: block; color: var(--brand-red); text-decoration: none;
    font-size: 16px; line-height: 20px; padding: 7px 0 12px 11px;
    border-bottom: 1px dashed var(--white);
  }
  .main-nav a:last-child { border-bottom: none; }

  .feature-visual { position: absolute; left: 0; top: 0; width: 1200px; height: 900px; pointer-events: none; }

  .search-form { position: absolute; left: 939px; top: 226px; }
  .search-field { position: absolute; left: 0; top: 0; width: 154px; height: 23px; background: var(--field-grey); border: none; }
  .search-button {
    position: absolute; left: 162px; top: 0; width: 72px; height: 23px;
    background: var(--brand-red); color: var(--white); border: none;
    font-family: inherit; font-size: 15px; line-height: 23px;
  }
  .search-hint { position: absolute; left: 0; top: 31px; width: 200px; height: 22px; }
  .search-hint svg { position: absolute; left: 0; top: 2px; }
  .search-hint span { position: absolute; left: 46px; top: 0; color: var(--white); font-size: 14px; white-space: nowrap; }

  .tagline {
    position: absolute; left: 380px; top: 659px; width: 450px;
    text-align: center; color: var(--ink); font-size: 16px; line-height: 31px;
  }

  .site-footer { position: absolute; left: 0; top: 785px; width: 1200px; height: 115px; background: var(--black); }
  .footer-nav {
    position: absolute; right: 36px; top: 50px;
    color: var(--footer-grey); font-size: 14px; white-space: nowrap;
  }
  .footer-nav a { color: var(--footer-grey); text-decoration: none; }
  .footer-nav .divider { margin: 0 14px; }
</style>
</head>
<body>
  <header class="site-header">
    <div class="brand-name">Harbourline Residence Suites</div>
  </header>
  <div class="header-stripe"></div>
  <main class="page-body"></main>

  <svg class="feature-visual" width="1200" height="900" viewBox="0 0 1200 900" xmlns="http://www.w3.org/2000/svg">
    <defs>
      <filter id="soft-shadow" x="-10%" y="-10%" width="120%" height="120%">
        <feGaussianBlur stdDeviation="4"/>
      </filter>
      <linearGradient id="sky-tones" x1="0" y1="0" x2="0" y2="1">
        <stop offset="0" stop-color="#4f6fc4"/>
        <stop offset="0.55" stop-color="#8a9ad6"/>
        <stop offset="0.85" stop-color="#c2b2d6"/>
        <stop offset="1" stop-color="#6d7cb8"/>
      </linearGradient>
    </defs>
    <rect class="photo-shadow" x="337" y="227" width="576" height="356" fill="#2e2708" filter="url(#soft-shadow)"/>
    <g transform="rotate(-10.9 638 386)">
      <rect class="feature-photo" role="img" aria-label="Photo of a tall sail-shaped waterfront hotel tower at dusk against a blue sky"
            x="371" y="196" width="534" height="379" rx="3" fill="url(#sky-tones)" stroke="#9b1408" stroke-width="5"/>
    </g>
  </svg>

  <nav class="main-nav">
    <a href="#">HOME</a>
    <a href="#">APARTMENTS</a>
    <a href="#">RESERVATIONS</a>
    <a href="#">FAQ’S</a>
    <a href="#">CONTACT US</a>
  </nav>

  <form class="search-form">
    <input class="search-field" type="text" aria-label="Search destination">
    <button class="search-button" type="button">search</button>
    <div class="search-hint">
      <svg width="32" height="20" viewBox="0 0 32 20">
        <polygon points="0,0 9,0 18,10 9,20 0,20 9,10" fill="#9b1408"/>
        <polygon points="12,0 21,0 31,10 21,20 12,20 21,10" fill="#9b1408"/>
      </svg>
      <span>Search Destination</span>
    </div>
  </form>

  <p class="tagline">World wide short stay serviced Apartments for<br>Business and individual travellers.</p>

  <footer class="site-footer">
    <div class="footer-nav">
      <a href="#">HOME</a><span class="divider">|</span><a href="#">SEARCH</a><span class="divider">|</span><a href="#">CONTACT US</a><span class="divider">|</span><a href="#">PRIVACY &amp; POLICY</a><span class="divider">|</span><a href="#">COPYRIGHT</a>
    </div>
  </footer>
</body>
</html>
```